Woman owned consulting company needs an elegant and modern business card design

I need a business card design for my new consulting company, Mira Holcombe Consulting. I am looking for something that is simple and elegant, but also creative and original. You can use either version of the logo that are attached. I have also included the information that needs to be featured on the business card.

Contact Information for Business Card

Requirements
Must have
• The logo and the font type and a standard business card size. Use shades of gray/silver and or rose gold that are in the logo.
• I didn't realize that my actual logo wasn't attached. Please incorporate in the designs.
Should not have
• Colors that are different from my logo

```html
<!DOCTYPE html>
<html lang="en">
<head>
<meta charset="utf-8">
<title>Mira Holcombe Consulting – Business Card</title>
<link href="https://fonts.googleapis.com/css2?family=Open+Sans:wght@300;400;600&display=swap" rel="stylesheet">
<style>
  :root {
    --canvas: #ffffff;
    --card-light: #ffffff;
    --silver: #a9abb0;
    --silver-light: #c9cbcf;
    --ink: #3a3d48;
    --ink-soft: #9b9ea4;
    --white: #ffffff;
  }
  * { margin: 0; padding: 0; box-sizing: border-box; }
  html, body {
    width: 1200px; height: 1200px; overflow: hidden;
    background: var(--canvas);
    font-family: "Open Sans", Arial, sans-serif;
  }
  .canvas { position: relative; width: 1200px; height: 1200px; }

  .card { position: absolute; top: 421px; width: 533px; height: 330px; }
  .card--front { left: 47px; }
  .card--back { left: 596px; }
  .card__shape { position: absolute; inset: 0; overflow: visible; }
  .card--front .card__shape { filter: drop-shadow(0 3px 5px rgba(0,0,0,0.25)); }
  .card--back .card__shape { filter: drop-shadow(2px 4px 6px rgba(0,0,0,0.22)); }

  .abs { position: absolute; white-space: nowrap; }

  .company { left: 47px; top: 88px; font-size: 13px; color: var(--silver-light); }

  .brand-name { font-weight: 300; font-size: 26px; line-height: 1; color: var(--silver); }
  .card--front .brand-name { left: 47px; top: 152px; }
  .card--back .brand-name { left: 32px; top: 140px; }

  .divider { position: absolute; width: 1px; top: 69px; height: 192px; background: var(--silver); }

  .social { left: 277px; top: 123px; display: flex; gap: 13px; }
  .social__tile { width: 35px; height: 35px; background: var(--white); border-radius: 3px; }

  .contact-line { left: 277px; display: flex; align-items: center; gap: 11px; font-size: 12px; font-weight: 600; color: var(--white); }
  .contact-line__dot { width: 10px; height: 10px; border-radius: 50%; background: var(--silver-light); }

  .name { left: 247px; top: 103px; font-size: 34px; color: var(--ink); }
  .role { left: 247px; top: 148px; font-size: 21px; color: var(--ink-soft); }
  .cell { left: 247px; top: 178px; font-size: 11.5px; color: var(--ink); }
  .address { left: 247px; top: 203px; font-size: 11px; color: var(--ink); line-height: 17px; }
  .address__label { font-size: 15px; }
</style>
</head>
<body>
<div class="canvas">

  <section class="card card--front">
    <svg class="card__shape" viewBox="0 0 533 330" width="533" height="330" aria-hidden="true">
      <defs>
        <linearGradient id="darkFace" x1="0" y1="0" x2="1" y2="1">
          <stop offset="0" stop-color="#3d404c"/>
          <stop offset="1" stop-color="#2d3039"/>
        </linearGradient>
      </defs>
      <path d="M6,0 H400 A133,133 0 0 1 533,133 V324 Q533,330 527,330 H133 A133,133 0 0 1 0,197 V6 Q0,0 6,0 Z" fill="url(#darkFace)"/>
      <path d="M13,9 H398 A126,126 0 0 1 524,135 V321 H135 A126,126 0 0 1 9,195 V13 Q9,9 13,9 Z" fill="none" stroke="#9fa2a8" stroke-width="1"/>
    </svg>
    <div class="abs company">Mira Holcombe Consulting, LLC</div>
    <div class="abs brand-name">Mira Holcombe</div>
    <div class="divider" style="left:248px"></div>
    <div class="divider" style="left:256px"></div>
    <div class="abs social">
      <span class="social__tile"></span>
      <span class="social__tile"></span>
      <span class="social__tile"></span>
    </div>
    <div class="abs contact-line" style="top:176px"><span class="contact-line__dot"></span>mira@miraholcombe.com</div>
    <div class="abs contact-line" style="top:193px"><span class="contact-line__dot"></span>www.miraholcombe.com</div>
  </section>

  <section class="card card--back">
    <svg class="card__shape" viewBox="0 0 533 330" width="533" height="330" aria-hidden="true">
      <path d="M6,0 H400 A133,133 0 0 1 533,133 V324 Q533,330 527,330 H133 A133,133 0 0 1 0,197 V6 Q0,0 6,0 Z" fill="var(--card-light)"/>
      <path d="M20,16 H398 A118,118 0 0 1 516,134 V316 H137 A118,118 0 0 1 19,198 V20 Q19,16 23,16 Z" fill="none" stroke="#6d7078" stroke-width="1"/>
    </svg>
    <div class="abs brand-name">Mira Holcombe</div>
    <div class="divider" style="left:221px"></div>
    <div class="divider" style="left:229px"></div>
    <div class="abs name">Mira Holcombe</div>
    <div class="abs role">Owner</div>
    <div class="abs cell">Cell: 610-555-0142</div>
    <div class="abs address"><span class="address__label">Address:</span> Unit 8, 140 Larkin Lane, Eastbrook,<br>WA, 6602</div>
  </section>

</div>
</body>
</html>
```